Business Card for new Overseas Property Buying Business

Hi

We need a new business card for our new business.

We are Faraway Nest Finders. So we search locations on behalf of our clients to find them the ideal home.

These are mainly holiday homes in nice locations - but sometimes people are looking to relocate.

I am looking for a nice simple design - that has some class and professionalism about it. Taking inspiration from our logo.

Text wise I was thinking of maybe having something like. (THE FONT FOR THIS SHOULD BE LIKE THE WRITING IN THE ATTACHMENT WITH THE MAP ON IT)

1)
What does your dream house have (tick all that apply):
swimming pool x
private vineyard x
herb garden x
full sized football pitch x

2)
How to buy a home abroad:

Method 1:
1) Scour internet for suitable estate agents
2) Arrange hectic holiday timetable with multiple agents in multiple languages
3) Fly to destination to find property was not as it seemed
4) Feel frustrated and helpless
OR
Method 2:
Contact your expert home hunter (details overleaf) - and leave the hard work to them

The end result should give people confidence that they are dealing with a professional organisation - and feel like they can place their trust in them. I would want it to drive them to either contact us directly or visit the website.

Please include name (Gordon Tramley), position (founder), contact numbers x 2, email address, website (www.quelvatrix-moor.com)

I look forward to seeing your entries.

Reason: Hi Sorry to extend - Xmas has got in the way of my plans. I will be providing feedback. Happy Christmas to you all.

```html
<!DOCTYPE html>
<html lang="en">
<head>
<meta charset="utf-8">
<title>Faraway Nest Finders – Business Card</title>
<link rel="stylesheet" href="https://fonts.googleapis.com/css2?family=Sorts+Mill+Goudy&family=Crimson+Text:wght@400;600;700&family=Handlee&display=swap">
<style>
  :root {
    --backdrop: #ece7e0;
    --card: #ffffff;
    --ink-brown: #4a3a30;
    --ink-dark: #2f2a26;
    --accent-orange: #e8643a;
    --accent-terracotta: #d9553b;
    --watermark: #e7a58a;
    --rule: #6b5a4e;
    --script-ink: #1f1f24;
    --shadow: rgba(40, 25, 10, 0.28);
  }
  * { box-sizing: border-box; margin: 0; padding: 0; }
  html, body {
    width: 1200px;
    height: 960px;
    overflow: hidden;
    background: var(--backdrop);
  }
  .canvas {
    position: relative;
    width: 1200px;
    height: 960px;
  }
  .card {
    position: absolute;
    background: var(--card);
    box-shadow: 0 6px 18px var(--shadow);
    overflow: hidden;
  }

  /* Front of card */
  .card-front {
    left: 70px;
    top: 60px;
    width: 720px;
    height: 410px;
  }
  .brand-watermark {
    position: absolute;
    left: 350px;
    top: 30px;
    width: 480px;
    height: 480px;
    opacity: 0.22;
  }
  .brand-mark {
    position: absolute;
    left: 130px;
    top: 70px;
    width: 170px;
    height: 170px;
  }
  .brand {
    position: absolute;
    left: 52px;
    top: 290px;
    width: 370px;
  }
  .brand-name {
    font-family: "Sorts Mill Goudy", "Crimson Text", serif;
    font-size: 44px;
    line-height: 1;
    color: var(--ink-dark);
    white-space: nowrap;
  }
  .brand-rule {
    height: 2px;
    background: var(--rule);
    margin: 8px 0 6px;
  }
  .brand-tagline {
    font-family: "Crimson Text", serif;
    font-size: 22px;
    font-weight: 600;
    letter-spacing: 0.5px;
    color: var(--ink-dark);
    text-transform: uppercase;
    text-align: center;
    white-space: nowrap;
  }
  .contact {
    position: absolute;
    right: 48px;
    top: 70px;
    text-align: right;
    font-family: "Crimson Text", serif;
    color: var(--ink-brown);
  }
  .contact-name {
    font-size: 32px;
    font-weight: 700;
    line-height: 1.1;
  }
  .contact-role {
    font-size: 24px;
    font-weight: 700;
    color: var(--accent-orange);
    margin-bottom: 8px;
  }
  .contact-line {
    font-size: 24px;
    line-height: 1.3;
  }
  .contact-web {
    position: absolute;
    right: 48px;
    bottom: 50px;
    font-family: "Crimson Text", serif;
    font-size: 22px;
    color: var(--ink-brown);
  }

  /* Back of card */
  .card-back {
    left: 440px;
    top: 520px;
    width: 700px;
    height: 390px;
    padding: 20px 32px;
    font-family: "Handlee", cursive;
    font-size: 20px;
    line-height: 1.13;
    color: var(--script-ink);
  }
  .quiz { margin-bottom: 12px; }
  .quiz-options span { margin-right: 34px; }
  .method-list { list-style: none; }
</style>
</head>
<body>
<main class="canvas">

  <section class="card card-front" aria-label="Business card front">
    <svg class="brand-watermark" viewBox="0 0 480 480" aria-hidden="true">
      <circle cx="240" cy="240" r="235" fill="var(--watermark)"/>
    </svg>

    <svg class="brand-mark" viewBox="0 0 170 170" aria-hidden="true">
      <circle cx="85" cy="85" r="80" fill="var(--accent-terracotta)"/>
    </svg>

    <div class="brand">
      <div class="brand-name">Quelvatrix &amp; Moor</div>
      <div class="brand-rule"></div>
      <div class="brand-tagline">Faraway Nest Finders</div>
    </div>

    <div class="contact">
      <div class="contact-name">Gordon Tramley</div>
      <div class="contact-role">Founder</div>
      <div class="contact-line">555-555-5555</div>
      <div class="contact-line">555-555-5555</div>
      <div class="contact-line">gordon@quelvatrix-moor.com</div>
    </div>

    <div class="contact-web">www.quelvatrix-moor.com</div>
  </section>

  <section class="card card-back" aria-label="Business card back">
    <div class="quiz">
      <p>What does your dream house have (tick all that apply):</p>
      <p class="quiz-options">
        <span>swimming pool x</span><span>private vineyard x</span><span>herb garden x</span>
      </p>
      <p>full sized football pitch x</p>
    </div>

    <div class="methods">
      <p>How to buy a home abroad:</p>
      <p>Method 1:</p>
      <ol class="method-list">
        <li>1) Scour internet for suitable estate agents</li>
        <li>2) Arrange hectic holiday timetable with multiple agents in<br>multiple languages</li>
        <li>3) Fly to destination to find property was not as it seemed</li>
        <li>4) Feel frustrated and helpless</li>
      </ol>
      <p>OR</p>
      <p>Method 2:</p>
      <p>Contact your expert home hunter (details overleaf) – and<br>leave the hard work to them</p>
    </div>
  </section>

</main>
</body>
</html>
```